World Wide News and Current Affairs website

We intends to start up a new website which deals on New and Current Affairs.
Attention Designers,
We want a home page design for this project. Our business is based in the United States. Our goal is to become a well known brand.
The website would consist of a category for News, Business and Tech.
The theme should be beautiful and attention seeking. The website would take bulk of it's news from the US, and Europe.
Designers can get inspiration from already existing new websites such as ZPW, VJL, HALDRIM.
All designs should be clean and easy to navigate.

```html
<!DOCTYPE html>
<html lang="en">
<head>
<meta charset="utf-8">
<title>News Home</title>
<link rel="stylesheet" href="https://fonts.googleapis.com/css2?family=Montserrat:wght@400;700&family=Droid+Serif:wght@700&display=swap">
<style>
:root{
  --ink:#1d1d1d;
  --bar:#222527;
  --bar-active:#1a1c1e;
  --orange:#f28a00;
  --page:#ececec;
  --white:#ffffff;
  --muted:#9a9a9a;
  --body:#6b6b6b;
  --ad:#c9c9c9;
  --footer:#1e1e1e;
}
*{margin:0;padding:0;box-sizing:border-box}
html,body{width:802px;height:1200px;overflow:hidden}
body{position:relative;background:var(--page);font-family:"Montserrat",sans-serif;color:var(--ink)}
.abs{position:absolute}
.site-header{left:0;top:0;width:802px;height:30px;background:var(--bar)}
.brand{left:175px;top:4px;font-weight:700;font-size:17px;color:var(--orange)}
.nav a{position:absolute;top:0;height:30px;line-height:30px;font-size:5.5px;font-weight:700;color:var(--white);text-decoration:none;letter-spacing:.3px;text-align:center}
.nav .active{background:var(--bar-active);border-bottom:2px solid var(--orange)}
.hero-photo{position:absolute}
.hero-main{left:0;top:30px;width:436px;height:221px;background:linear-gradient(120deg,#3a4a66 0%,#2a3142 45%,#4a4b55 100%)}
.hero-tile{width:191px;height:111px;background:linear-gradient(160deg,#9aa9b6 0%,#6f8597 55%,#4d6174 100%)}
.hero-shade{position:absolute;inset:0;background:linear-gradient(180deg,rgba(0,0,0,0) 30%,rgba(0,0,0,.55) 100%)}
.hero-text{position:absolute;color:var(--white)}
.hero-date{font-size:7px}
.hero-title{font-family:"Droid Serif",serif;font-weight:700;color:var(--white);line-height:1.15}
.hero-body{font-size:6.6px;line-height:1.35;margin-top:6px}
.by{font-size:5.5px;color:var(--muted)}
.hero-text .by{color:var(--white)}
.by b{font-weight:400;color:var(--orange)}
.tabs-bar{left:0;top:251px;width:802px;height:21px;background:var(--white);border-bottom:1px solid #dcdcdc}
.tab{position:absolute;top:0;height:21px;line-height:21px;font-size:7.5px;font-weight:700}
.tab.on{left:176px;width:51px;background:var(--orange);color:var(--white);text-align:center}
.card-img{background:var(--ink);height:90px;width:152px}
.card-strip{height:4px;width:152px;background:var(--white)}
.card-date{font-size:4.5px;color:var(--muted);margin:4px 0 0 7px}
.card-title{font-family:"Droid Serif",serif;font-size:10.2px;line-height:1.15;margin:3px 0 0 7px;font-weight:700}
.card-body{font-size:5.6px;line-height:1.5;color:var(--body);margin:9px 0 0 8px;width:136px}
.card .by{margin:14px 0 0 8px}
.ad{left:502px;top:282px;width:126px;height:105px;background:var(--ad);color:var(--white);font-size:7px;text-align:center;line-height:105px}
.side-tabs{left:502px;top:399px;width:126px;height:22px;background:var(--ink)}
.side-tabs span{position:absolute;top:0;line-height:22px;font-size:5.5px;color:var(--white)}
.side-list{left:502px;top:425px;width:126px;height:207px;background:var(--white)}
.side-item{position:absolute;left:8px;display:flex;gap:6px;align-items:center}
.dot{width:10px;height:10px;border-radius:50%;background:var(--ink);flex:none}
.side-item p{font-size:4.6px;line-height:1.2;color:#aaa}
.row{position:absolute;left:176px;width:320px;height:84px}
.row-img{position:absolute;left:0;top:0;width:93px;height:84px;background:var(--ink)}
.row-text{position:absolute;left:103px;top:9px}
.row-title{font-family:"Droid Serif",serif;font-weight:700;font-size:10.2px;margin-top:3px}
.row-body{font-size:5.6px;line-height:1.45;color:#444;margin-top:5px;width:200px}
.row .by{margin-top:14px}
.page{position:absolute;top:1119px;height:16px;line-height:16px;font-size:6px;font-weight:700;color:var(--white);text-align:center;background:var(--ad)}
.page.on{background:var(--orange)}
.site-footer{left:0;top:1157px;width:802px;height:43px;background:var(--footer)}
</style>
</head>
<body>
<header class="site-header abs">
  <div class="brand abs">Logo</div>
  <nav class="nav">
    <a class="active" style="left:419px;width:45px">HOME</a>
    <a style="left:474px;width:24px">NEWS</a>
    <a style="left:518px;width:34px">ABOUT US</a>
    <a style="left:575px;width:41px">CONTACT US</a>
  </nav>
</header>

<section class="hero">
  <div class="hero-photo hero-main" role="img" aria-label="Stock exchange trading floor with a trader wearing a headset">
    <div class="hero-shade"></div>
    <div class="hero-text" style="left:176px;top:110px;width:250px">
      <div class="hero-date">April 23, 2015</div>
      <h2 class="hero-title" style="font-size:13px;margin-top:8px">Lorem ipsum dolor sit amet,<br>consectetur adipiscing elit.</h2>
      <p class="hero-body">Nunc aliquam euismod lectus. Lorem ipsum dolor sit amet, consecte-tur adipiscing elit. Suspendisse nec libero nibh. Ut non velit velit. Nulla id egestas felis. Fusce vestibulum lacinia enim.</p>
      <div class="by" style="margin-top:14px">By <b>John Doe</b></div>
    </div>
  </div>
  <div class="hero-photo hero-tile" style="left:436px;top:30px" role="img" aria-label="White robot in an office"><div class="hero-shade"></div>
    <div class="hero-text" style="left:13px;top:46px"><div class="hero-date">April 23, 2015</div><h3 class="hero-title" style="font-size:9.6px">Lorem ipsum dolor sit amet,<br>consectetur adipiscing elit.</h3><div class="by" style="margin-top:14px">By <b>John Doe</b></div></div></div>
  <div class="hero-photo hero-tile" style="left:627px;top:30px;width:175px" role="img" aria-label="Delivery drone flying in the sky"><div class="hero-shade"></div>
    <div class="hero-text" style="left:13px;top:46px"><div class="hero-date">April 23, 2015</div><h3 class="hero-title" style="font-size:9.6px">Lorem ipsum dolor sit amet,<br>consectetur adipiscing elit.</h3><div class="by" style="margin-top:14px">By <b>John Doe</b></div></div></div>
  <div class="hero-photo hero-tile" style="left:436px;top:141px;height:110px" role="img" aria-label="Delivery drone flying in the sky"><div class="hero-shade"></div>
    <div class="hero-text" style="left:13px;top:48px"><div class="hero-date">April 23, 2015</div><h3 class="hero-title" style="font-size:9.6px">Lorem ipsum dolor sit amet,<br>consectetur adipiscing elit.</h3><div class="by" style="margin-top:14px">By <b>John Doe</b></div></div></div>
  <div class="hero-photo hero-tile" style="left:627px;top:141px;width:175px;height:110px" role="img" aria-label="White robot in an office"><div class="hero-shade"></div>
    <div class="hero-text" style="left:12px;top:48px"><div class="hero-date">April 23, 2015</div><h3 class="hero-title" style="font-size:9.6px">Lorem ipsum dolor sit amet,<br>consectetur adipiscing elit.</h3><div class="by" style="margin-top:14px">By <b>John Doe</b></div></div></div>
</section>

<div class="tabs-bar abs">
  <span class="tab on">ALL</span>
  <span class="tab" style="left:240px;color:var(--orange)">BUSINESS</span>
  <span class="tab" style="left:304px;color:#b5b5b5;font-weight:400">TECH</span>
</div>

<article class="card abs" style="left:176px;top:282px">
  <div class="card-img" role="img" aria-label="Article image"></div><div class="card-strip"></div>
  <div class="card-date">April 23, 2015</div>
  <h3 class="card-title">Lorem ipsum dolor sit amet,<br>consectetur adipiscing elit.</h3>
  <p class="card-body">Etiam hendrerit augue id augue luctus facilisis. Aenean laoreet dignissim imperdi-et. Cras quis nibh vitae tortor eleifend tempus. Integer convallis quam ipsum, quis aliquet quam iaculis eu. giat lectus.</p>
  <div class="by">By <b>John Doe</b></div>
</article>
<article class="card abs" style="left:339px;top:282px">
  <div class="card-img" role="img" aria-label="Article image"></div><div class="card-strip"></div>
  <div class="card-date">April 23, 2015</div>
  <h3 class="card-title">Lorem ipsum dolor sit amet,<br>consectetur adipiscing elit.</h3>
  <p class="card-body">Etiam hendrerit augue id augue luctus facilisis. Aenean laoreet dignissim imperdi-et. Cras quis nibh vitae tortor eleifend tempus. Integer convallis quam ipsum, quis aliquet quam iaculis eu. giat lectus.</p>
  <div class="by">By <b>John Doe</b></div>
</article>
<article class="card abs" style="left:176px;top:505px">
  <div class="card-img" role="img" aria-label="Article image"></div>
  <div class="card-date" style="margin-top:8px">April 23, 2015</div>
  <h3 class="card-title">Lorem ipsum dolor sit amet,<br>consectetur adipiscing elit.</h3>
  <p class="card-body">Etiam hendrerit augue id augue luctus facilisis. Aenean laoreet dignissim imperdi-et. Cras quis nibh vitae tortor eleifend tempus. Integer convallis quam ipsum, quis aliquet quam iaculis eu. giat lectus.</p>
  <div class="by">By <b>John Doe</b></div>
</article>
<article class="card abs" style="left:339px;top:505px">
  <div class="card-img" role="img" aria-label="Article image"></div>
  <div class="card-date" style="margin-top:8px">April 23, 2015</div>
  <h3 class="card-title">Lorem ipsum dolor sit amet,<br>consectetur adipiscing elit.</h3>
  <p class="card-body">Etiam hendrerit augue id augue luctus facilisis. Aenean laoreet dignissim imperdi-et. Cras quis nibh vitae tortor eleifend tempus. Integer convallis quam ipsum, quis aliquet quam iaculis eu. giat lectus.</p>
  <div class="by">By <b>John Doe</b></div>
</article>

<aside>
  <div class="ad abs">300x250 ad</div>
  <div class="side-tabs abs">
    <span style="left:0;width:30px;background:var(--orange);text-align:center">Popular</span>
    <span style="left:36px">General</span>
  </div>
  <div class="side-list abs">
    <div class="side-item" style="top:4px"><span class="dot"></span><p>Sed posuere lobortis consectetur.<br>Nulla facilisi, fusce arcu libero.</p></div>
    <div class="side-item" style="top:29px"><span class="dot"></span><p>Sed posuere lobortis consectetur.<br>Nulla facilisi, fusce arcu libero.</p></div>
    <div class="side-item" style="top:54px"><span class="dot"></span><p>Sed posuere lobortis consectetur.<br>Nulla facilisi, fusce arcu libero.</p></div>
    <div class="side-item" style="top:79px"><span class="dot"></span><p>Sed posuere lobortis consectetur.<br>Nulla facilisi, fusce arcu libero.</p></div>
    <div class="side-item" style="top:108px"><span class="dot"></span><p>Sed posuere lobortis consectetur.<br>Nulla facilisi, fusce arcu libero.</p></div>
    <div class="side-item" style="top:133px"><span class="dot"></span><p>Sed posuere lobortis consectetur.<br>Nulla facilisi, fusce arcu libero.</p></div>
    <div class="side-item" style="top:158px"><span class="dot"></span><p>Sed posuere lobortis consectetur.<br>Nulla facilisi, fusce arcu libero.</p></div>
    <div class="side-item" style="top:183px"><span class="dot"></span><p>Sed posuere lobortis consectetur.<br>Nulla facilisi, fusce arcu libero.</p></div>
  </div>
</aside>

<section class="list">
  <article class="row" style="top:726px"><div class="row-img" role="img" aria-label="Article image"></div><div class="row-text"><div class="card-date" style="margin:0">April 23, 2015</div><h3 class="row-title">Lorem ipsum dolor sit amet.</h3><p class="row-body">Etiam hendrerit augue id augue luctus facilisis. Aenean laoreet dignissim imperdiet. Cras.</p><div class="by">By <b>John Doe</b></div></div></article>
  <article class="row" style="top:821px"><div class="row-img" role="img" aria-label="Article image"></div><div class="row-text"><div class="card-date" style="margin:0">April 23, 2015</div><h3 class="row-title">Lorem ipsum dolor sit amet.</h3><p class="row-body">Etiam hendrerit augue id augue luctus facilisis. Aenean laoreet dignissim imperdiet. Cras.</p><div class="by">By <b>John Doe</b></div></div></article>
  <article class="row" style="top:917px"><div class="row-img" role="img" aria-label="Article image"></div><div class="row-text"><div class="card-date" style="margin:0">April 23, 2015</div><h3 class="row-title">Lorem ipsum dolor sit amet.</h3><p class="row-body">Etiam hendrerit augue id augue luctus facilisis. Aenean laoreet dignissim imperdiet. Cras.</p><div class="by">By <b>John Doe</b></div></div></article>
  <article class="row" style="top:1013px"><div class="row-img" role="img" aria-label="Article image"></div><div class="row-text"><div class="card-date" style="margin:0">April 23, 2015</div><h3 class="row-title">Lorem ipsum dolor sit amet.</h3><p class="row-body">Etiam hendrerit augue id augue luctus facilisis. Aenean laoreet dignissim imperdiet. Cras.</p><div class="by">By <b>John Doe</b></div></div></article>
</section>

<nav class="pager">
  <span class="page on" style="left:176px;width:16px">1</span>
  <span class="page" style="left:197px;width:16px">2</span>
  <span class="page" style="left:218px;width:27px">Next</span>
</nav>

<footer class="site-footer abs"></footer>
</body>
</html>
```